New Podcast focussing on non-mainstream interventions for guidance needs podcast art

I need an exquisite piece of podcast art work for the launch of my new podcast 'Past the Hollow'. This podcast explores unorthodox, esoteric and unconventional methods to find peace, clarity and direction in life. Topics include family Constellations Systems, Psychedelics, Equine Therapy and Floatation to name a few. A teaser has been posted on Brevlo with a strong response. The audience is primarily midlifers or those in a career/personal crisis of direction. It's meant to comfort, inform and empower and offer other ways rather than mainstream to work out what to do with your life. The file shared with you shows the pic used on Brevlo as it's illustrating the idea of illumination. You can use it or not, and whilst I am ex-Military, I don't want the cover to convey an overly military influence. I'd like 'Past the Hollow' to feature on the art work and my name, Margot Pennick. I'd like inspiration, creativity, and the idea of hope conveyed as well as clarity and courage. Whilst the podcast is about finding your direction please do no use compass images or cross road images as that is too obvious.
Hope that all helps. Looking forward to your ideas.

```html
<!DOCTYPE html>
<html lang="en">
<head>
<meta charset="utf-8">
<title>Past the Hollow — Podcast Cover</title>
<link href="https://fonts.googleapis.com/css2?family=Lobster&family=Montserrat:ital,wght@0,400;1,300&display=swap" rel="stylesheet">
<style>
  :root {
    --page: #ffffff;
    --navy: #24284a;
    --ring-red: #9e1c35;
    --ring-orange: #eb711e;
    --ring-amber: #f4a22e;
    --ring-yellow: #f7c83a;
    --title: #f4a12b;
    --light: #ffffff;
  }
  html, body {
    margin: 0;
    padding: 0;
    width: 1200px;
    height: 1200px;
    overflow: hidden;
    background: var(--page);
  }
  .canvas {
    position: relative;
    width: 1200px;
    height: 1200px;
    background: var(--page);
  }
  .cover {
    position: absolute;
    left: 131px;
    top: 108px;
    width: 938px;
    height: 938px;
    background: var(--navy);
    overflow: hidden;
  }
  .label-row {
    position: absolute;
    left: 0;
    right: 0;
    top: 50px;
    height: 32px;
    display: flex;
    align-items: center;
  }
  .label-rule {
    flex: 1;
    height: 1.5px;
    background: var(--light);
    opacity: 0.9;
  }
  .label {
    font-family: "Montserrat", sans-serif;
    font-weight: 400;
    font-size: 27px;
    letter-spacing: 18px;
    color: var(--light);
    padding: 0 14px 0 32px;
    line-height: 1;
  }
  .artwork {
    position: absolute;
    left: 0;
    top: 0;
    width: 938px;
    height: 938px;
  }
  .title {
    position: absolute;
    left: 0;
    right: 0;
    top: 732px;
    margin: 0;
    text-align: center;
    font-family: "Lobster", cursive;
    font-weight: 400;
    font-size: 92px;
    line-height: 1.1;
    color: var(--title);
  }
  .host {
    position: absolute;
    left: 0;
    right: 0;
    top: 830px;
    margin: 0;
    text-align: center;
    font-family: "Montserrat", sans-serif;
    font-style: italic;
    font-weight: 300;
    font-size: 46px;
    letter-spacing: 1px;
    line-height: 1;
    color: var(--light);
  }
</style>
</head>
<body>
  <div class="canvas">
    <section class="cover">
      <svg class="artwork" viewBox="0 0 938 938" role="img"
           aria-label="Illustration: a figure in silhouette walking out of tall grass toward a large setting sun, with a pine tree at the left edge">
        <defs>
          <clipPath id="horizon-clip">
            <rect x="0" y="0" width="938" height="656"/>
          </clipPath>
        </defs>
        <g clip-path="url(#horizon-clip)">
          <circle cx="469" cy="421" r="279" fill="var(--ring-red)"/>
          <circle cx="469" cy="421" r="251" fill="var(--ring-orange)"/>
          <circle cx="469" cy="421" r="224" fill="var(--ring-amber)"/>
          <circle cx="469" cy="421" r="198" fill="var(--ring-yellow)"/>
        </g>
      </svg>

      <div class="label-row">
        <span class="label-rule"></span>
        <span class="label">PODCAST</span>
        <span class="label-rule"></span>
      </div>

      <h1 class="title">Past the Hollow</h1>
      <p class="host">MARGOT PENNICK</p>
    </section>
  </div>
</body>
</html>
```